Notary Signing Agent Need Business card Design

Need a Business card design for my new company. RT Velo-Brisk LLC
Mobile Notary Signing Agent. I go to the customer for closing of Mortgage's Documents . possible signs of honesty, integrity and confidentiality.

Work with Title company to Notary Mortgage closing.

My Target Market is Title companies. Banks and Financial Institution.

Color Blue to Black Professional ) if needed some Green Little Red

And possible a company logo.

Mobile ( travel to clients ) Integrity, Honest Trustworthy. A show of Professional services.

Would like company name and my name on card

Use both sides and front with business name and my name. phone numbers.

Target Market(s)

Title company, Banks mortgage company

Industry/Entity Type

Travel

Contact Information for Business Card

Notary, Certified signing agent, Mobile

Colors
0455a3

Requirements
Must have
• Name of company , owners name phone number,
Nice to have
• blue and black color like a professional look but not limit to these only.
• a stand out from other cards .

```html
<!DOCTYPE html>
<html lang="en">
<head>
<meta charset="utf-8">
<title>RT Velo-Brisk LLC — Business Card</title>
<link rel="stylesheet" href="https://fonts.googleapis.com/css2?family=Arimo:wght@400;700&display=swap">
<style>
  :root {
    --backdrop: #6d6e6e;
    --brand-blue: #0455a3;
    --brand-blue-light: #2a7cc7;
    --brand-blue-dark: #033f7d;
    --ink: #1a1a1a;
    --paper: #ffffff;
    --rule: #b9bcc0;
  }
  html, body {
    margin: 0;
    padding: 0;
    width: 1200px;
    height: 1200px;
    overflow: hidden;
    background: var(--backdrop);
    font-family: "Arimo", Arial, sans-serif;
  }
  .sheet {
    position: relative;
    width: 1200px;
    height: 1200px;
  }
  .card {
    position: absolute;
    left: 180px;
    width: 840px;
    height: 480px;
    overflow: hidden;
    box-shadow: 0 6px 18px rgba(0,0,0,0.25);
  }
  .card--front {
    top: 80px;
    background: radial-gradient(ellipse at 42% 38%, var(--brand-blue-light) 0%, var(--brand-blue) 55%, var(--brand-blue-dark) 100%);
  }
  .card--back {
    top: 640px;
    background: var(--paper);
  }
  .front-name {
    position: absolute;
    left: 56px;
    bottom: 70px;
    margin: 0;
    color: var(--paper);
    font-weight: 700;
    font-size: 46px;
    letter-spacing: 0.5px;
  }
  .back-company {
    position: absolute;
    left: 150px;
    top: 48px;
    margin: 0;
    color: var(--brand-blue);
    font-weight: 700;
    font-size: 34px;
  }
  .owner {
    position: absolute;
    right: 420px;
    top: 190px;
    text-align: right;
  }
  .owner-name {
    margin: 0;
    color: var(--brand-blue);
    font-weight: 700;
    font-size: 26px;
  }
  .owner-title {
    margin: 4px 0 0;
    color: var(--ink);
    font-weight: 700;
    font-size: 13px;
    letter-spacing: 1px;
  }
  .divider {
    position: absolute;
    left: 444px;
    top: 168px;
    width: 1px;
    height: 104px;
    background: var(--rule);
  }
  .contact-list {
    position: absolute;
    left: 470px;
    top: 168px;
    margin: 0;
    padding: 0;
    list-style: none;
  }
  .contact-item {
    display: flex;
    align-items: center;
    height: 34px;
    color: var(--ink);
    font-size: 20px;
  }
  .contact-icon {
    width: 20px;
    height: 20px;
    margin-right: 14px;
    fill: var(--brand-blue);
  }
  .footer-band {
    position: absolute;
    left: 0;
    bottom: 0;
    width: 840px;
    height: 110px;
  }
  .website {
    position: absolute;
    left: 0;
    right: 0;
    bottom: 10px;
    margin: 0;
    text-align: center;
    color: var(--paper);
    font-size: 19px;
  }
</style>
</head>
<body>
<main class="sheet">
  <section class="card card--front" aria-label="Card front">
    <h1 class="front-name">RT VELO-BRISK LLC.</h1>
  </section>

  <section class="card card--back" aria-label="Card back">
    <h2 class="back-company">RT VELO-BRISK LLC.</h2>

    <div class="owner">
      <p class="owner-name">DANIEL R HOLT</p>
      <p class="owner-title">OWNER</p>
    </div>

    <div class="divider"></div>

    <ul class="contact-list">
      <li class="contact-item">
        <svg class="contact-icon" viewBox="0 0 24 24" aria-hidden="true"><path d="M6.6 10.8c1.4 2.8 3.8 5.1 6.6 6.6l2.2-2.2c.3-.3.7-.4 1-.2 1.1.4 2.3.6 3.6.6.6 0 1 .4 1 1V20c0 .6-.4 1-1 1C10.6 21 3 13.4 3 4c0-.6.4-1 1-1h3.5c.6 0 1 .4 1 1 0 1.3.2 2.5.6 3.6.1.3 0 .7-.2 1z"/></svg>
        555-201-4438
      </li>
      <li class="contact-item">
        <svg class="contact-icon" viewBox="0 0 24 24" aria-hidden="true"><path d="M7 2h10a2 2 0 0 1 2 2v16a2 2 0 0 1-2 2H7a2 2 0 0 1-2-2V4a2 2 0 0 1 2-2zm0 3v12h10V5H7zm5 13.5a1 1 0 1 0 0 2 1 1 0 0 0 0-2z"/></svg>
        555-317-9062
      </li>
      <li class="contact-item">
        <svg class="contact-icon" viewBox="0 0 24 24" aria-hidden="true"><path d="M3 5h18a1 1 0 0 1 1 1v12a1 1 0 0 1-1 1H3a1 1 0 0 1-1-1V6a1 1 0 0 1 1-1zm1 2.3V17h16V7.3l-8 5.2-8-5.2zM5.6 7 12 11.2 18.4 7H5.6z"/></svg>
        email@mail.com
      </li>
    </ul>

    <svg class="footer-band" viewBox="0 0 840 110" aria-hidden="true">
      <path d="M0 18 Q420 62 840 18" fill="none" stroke="var(--rule)" stroke-width="2"/>
      <path d="M0 30 Q420 74 840 30 L840 110 L0 110 Z" fill="var(--brand-blue)"/>
    </svg>
    <p class="website">www.website.com</p>
  </section>
</main>
</body>
</html>
```